new construction company branding

branding

Can I have a banner made so I can hang it as 1) branding my jobsite 2) advertisement

Target Market(s)

Commercial

Industry/Entity Type

Construction Trade

Font styles to use
Other font styles liked:
• Cinzel bold

Colors
EB3D1F
EC4F4E
F09395
F8D3D4
FCEDEE

Requirements
Must have
• Bright colors for advertisement
Nice to have
• 36”x48” canvas
Should not have
• To busy

```html
<!DOCTYPE html>
<html lang="en">
<head>
<meta charset="utf-8">
<title>Northfield Build Co — General Contractor Flyer</title>
<link href="https://fonts.googleapis.com/css2?family=Rubik:wght@400;500;700;800&display=swap" rel="stylesheet">
<style>
  :root{
    --red:#e3121a;
    --ink:#111111;
    --body:#1a1a1a;
    --gray:#7a7a7a;
    --brand-gray:#5f5f5f;
    --paper:#ffffff;
    --bg:#7c7c7c;
    --tan:#e8cfae;
    --navy:#2d3f73;
  }
  *{margin:0;padding:0;box-sizing:border-box}
  html,body{width:1200px;height:1200px;overflow:hidden;background:var(--bg)}
  .canvas{position:relative;width:1200px;height:1200px}
  .flyer{
    position:absolute;left:176px;top:0;width:1051px;height:1486px;
    transform:scale(0.8075);transform-origin:0 0;
    background:var(--paper);overflow:hidden;
    font-family:"Rubik",Arial,sans-serif;color:var(--ink);
  }
  .hero-photo{
    position:absolute;left:300px;top:0;width:751px;height:720px;
    background:
      linear-gradient(90deg,#fff 0%,rgba(255,255,255,0) 38%),
      linear-gradient(90deg,var(--tan) 0%,#dcc09c 45%,#4a5680 62%,var(--navy) 80%,#b79a7a 100%);
  }
  .swoosh{position:absolute;left:0;top:0;width:1051px;height:1486px}
  .brand{
    position:absolute;left:90px;top:180px;width:450px;
    display:flex;align-items:center;justify-content:center;gap:12px;
    font-weight:500;font-size:30px;color:var(--brand-gray);letter-spacing:.5px;
  }
  .brand-mark{width:20px;height:20px;background:var(--red)}
  .headline{position:absolute;left:99px;top:348px;font-weight:800;line-height:1}
  .headline .line-1{font-size:54px;color:var(--ink)}
  .headline .line-2{font-size:82px;color:var(--red);margin-top:2px;letter-spacing:1px}
  .headline .line-3{font-size:60px;color:var(--red);margin-top:-4px}
  .services-title{
    position:absolute;left:92px;top:744px;width:342px;text-align:right;
    font-weight:400;font-size:37px;
  }
  .services-title span{color:var(--red)}
  .services-rule{position:absolute;left:92px;top:797px;width:338px;height:1.5px;background:#444}
  .service-list{position:absolute;left:53px;top:822px;width:381px;list-style:none}
  .service-list li{position:relative;padding-left:38px;margin-bottom:22px;font-size:16px;line-height:21px;text-align:justify;color:var(--body)}
  .service-list li::before{content:"";position:absolute;left:10px;top:24px;bottom:-22px;width:1.5px;background:var(--red)}
  .service-list li:last-child::before{bottom:-6px}
  .service-list .tick{position:absolute;left:1px;top:2px;width:21px;height:21px}
  .gallery{position:absolute;left:512px;top:740px;display:grid;grid-template-columns:220px 220px;gap:18px 23px}
  .gallery-cell{position:relative;width:220px;height:220px}
  .gallery-cell .label{
    position:absolute;left:0;right:0;top:176px;height:28px;
    background:rgba(227,18,26,.9);
    color:#fff;font-weight:500;font-size:17px;
    display:flex;align-items:center;justify-content:center;letter-spacing:.3px;
  }
  .ph-roof{background:linear-gradient(160deg,#d9d6d2,#6f6d6b 70%,#4a4846)}
  .ph-plumb{background:linear-gradient(200deg,#f1f1f1,#c9c9c9 50%,#6e7a92)}
  .ph-kitchen{background:linear-gradient(170deg,#e4e2de,#8a8683 60%,#3d3c3f)}
  .ph-electric{background:linear-gradient(150deg,#7a5a3a,#c8c6c2 45%,#3f4047)}
  .about{position:absolute;left:510px;top:1211px;width:463px;font-size:16px;line-height:21px;text-align:justify;color:var(--body)}
  .footer{position:absolute;left:0;top:1351px;width:1051px;height:135px}
  .footer-shapes{position:absolute;inset:0;width:100%;height:100%}
  .footer-address{
    position:absolute;left:54px;top:25px;color:#fff;
    font-size:23px;line-height:28.5px;font-weight:400;
  }
  .footer-address strong{font-weight:700}
  .footer-contact{position:absolute;left:516px;top:22px;color:#fff;line-height:1}
  .footer-contact .phone{font-size:42px;font-weight:400}
  .footer-contact .phone strong{font-weight:700}
  .footer-contact .web{font-size:32px;margin-top:6px}
</style>
</head>
<body>
<div class="canvas">
  <div class="flyer">
    <div class="hero-photo" role="img" aria-label="Smiling contractor in cap and navy work shirt holding a clipboard beside a house"></div>

    <svg class="swoosh" viewBox="0 0 1051 1486" aria-hidden="true">
      <path d="M0,760 Q300,622 660,608 Q900,604 1051,690 L1051,1486 L0,1486 Z" fill="var(--red)"/>
      <path d="M0,840 Q330,642 660,632 Q900,628 1051,692 L1051,1486 L0,1486 Z" fill="var(--paper)"/>
    </svg>

    <div class="brand"><span class="brand-mark"></span>NORTHFIELD BUILD CO LLC</div>

    <h1 class="headline">
      <div class="line-1">NORTHFIELD</div>
      <div class="line-2">GENERAL</div>
      <div class="line-3">CONTRACTOR</div>
    </h1>

    <h2 class="services-title">OUR <span>SERVICES</span></h2>
    <div class="services-rule"></div>

    <ul class="service-list">
      <li><svg class="tick" viewBox="0 0 20 20"><circle cx="10" cy="10" r="10" fill="var(--red)"/><path d="M5.5 10.5l3 3 6-6.5" fill="none" stroke="#fff" stroke-width="2.2"/></svg>Lorem ipsum dolor sit amet, consectetur adipiscing elit. Quid autem habent admi­rationis, cum prope accesseris?</li>
      <li><svg class="tick" viewBox="0 0 20 20"><circle cx="10" cy="10" r="10" fill="var(--red)"/><path d="M5.5 10.5l3 3 6-6.5" fill="none" stroke="#fff" stroke-width="2.2"/></svg>Varietates autem iniurasque fortunae facile veteres philosophorum praeceptis instituta vita superabat. Et quod est munus, quod opus sapientiae?</li>
      <li><svg class="tick" viewBox="0 0 20 20"><circle cx="10" cy="10" r="10" fill="var(--red)"/><path d="M5.5 10.5l3 3 6-6.5" fill="none" stroke="#fff" stroke-width="2.2"/></svg>Duo Reges: constructio interrete. Quia nec honesto quic quam honestius nec turpi turpius. Tria genera bonorum</li>
      <li><svg class="tick" viewBox="0 0 20 20"><circle cx="10" cy="10" r="10" fill="var(--red)"/><path d="M5.5 10.5l3 3 6-6.5" fill="none" stroke="#fff" stroke-width="2.2"/></svg>Verum tamen cum de rebus grandioribus dicas, ipsae res verba rapiunt; Hoc non est positum in nostra actione.</li>
      <li><svg class="tick" viewBox="0 0 20 20"><circle cx="10" cy="10" r="10" fill="var(--red)"/><path d="M5.5 10.5l3 3 6-6.5" fill="none" stroke="#fff" stroke-width="2.2"/></svg>Equidem etiam Epicurum, in physicis quidem, Democriteum puto. Respondeat totidem verbis. Nemo igitur esse beatus potest. Consequens.</li>
    </ul>

    <div class="gallery">
      <div class="gallery-cell ph-roof" role="img" aria-label="Roofer in hard hat and safety vest working on shingles"><div class="label">TAMEN EXPETITUR</div></div>
      <div class="gallery-cell ph-plumb" role="img" aria-label="Plumber fixing pipes under a sink"><div class="label">HONESTO QUIC</div></div>
      <div class="gallery-cell ph-kitchen" role="img" aria-label="Worker installing kitchen cabinets"><div class="label">PUBLICA LIBRIS</div></div>
      <div class="gallery-cell ph-electric" role="img" aria-label="Electrician testing a breaker panel with a meter"><div class="label">PRAESTARE VITAM</div></div>
    </div>

    <p class="about">Lorem ipsum dolor sit amet, consectetur adipiscing elit. Quid autem habent admirationis, cum prope accesseris? An hoc usque quaque, aliter in vita? Non igitur de improbo, sed de callido improbo quaerimus, qualis Q. Nam quibus rebus efficiuntur voluptates,</p>

    <footer class="footer">
      <svg class="footer-shapes" viewBox="0 0 1051 135" preserveAspectRatio="none" aria-hidden="true">
        <rect x="0" y="0" width="1051" height="135" fill="var(--gray)"/>
        <polygon points="478,0 1051,0 1051,135 410,135" fill="var(--paper)"/>
        <polygon points="494,0 1051,0 1051,135 426,135" fill="var(--red)"/>
      </svg>
      <div class="footer-address">
        <strong>NORTHFIELD BUILD CO LLC</strong><br>
        4120 BIRCHWOOD RIDGE LANE<br>
        ANCHORAGE, ALASKA 99507
      </div>
      <div class="footer-contact">
        <div class="phone">CALL US <strong>555.214.0387</strong></div>
        <div class="web">WWW.NORTHFIELDBUILD.COM</div>
      </div>
    </footer>
  </div>
</div>
</body>
</html>
```